Harbor of Kitchencraft Podcast Episode Cover

I’m looking for a clean, professional, and eye-catching podcast episode cover template for my show, Harbor of Kitchencraft. Each week, I feature a new guest, so the design must allow me (or my team) to easily swap in a new guest’s photo without needing advanced design skills.

The template should be:

- Drag-and-drop friendly: simple for me to replace the guest’s headshot in Canva, Photoshop, or similar.
- On-brand with the Harbor of Kitchencraft podcast: professional yet approachable, foodservice industry-focused.
- Bold and attention-grabbing for podcast platforms and social media.

Readable text at small sizes, since covers are often viewed as thumbnails.

Design Elements to Include:

1. Podcast Title: “Harbor of Kitchencraft” (prominently displayed)
2. Subtitle/Space: Line for guest’s name, professional title, and company name
3. Photo Placeholder: Large, central area where I can easily drag and drop a guest photo
4. Brand Colors: attached
5. Clean, modern fonts (easy to read at thumbnail size)
6. Background graphics or patterns that give a sense of foodservice, leadership, or nationwide reach... but do not overpower the guest photo

Format Requirements:

- Editable source file (PSD, Canva template, or layered AI/INDD)
- JPG/PNG exports for immediate use
- Square format (3000x3000px) for podcast platforms

Style Inspiration:
Think modern podcast covers: bold fonts, clean lines, professional with a touch of energy.

Deliverables:

1. Final episode cover template (editable file)
2. Instructions or guidance on how to swap out guest photos

```html
<!DOCTYPE html>
<html lang="en">
<head>
<meta charset="utf-8">
<title>Harbor of Kitchencraft – Episode Cover</title>
<link href="https://fonts.googleapis.com/css2?family=Bebas+Neue&family=Poppins:wght@400;500;700&family=Yellowtail&display=swap" rel="stylesheet">
<style>
  :root {
    --navy: #1b3750;
    --navy-ring: #23465c;
    --grid-line: #173047;
    --gold: #f3b31a;
    --white: #ffffff;
    --placeholder: #d6d6d6;
    --placeholder-text: #444444;
    --gear-light: #8d939b;
    --gear-dark: #2a2d32;
  }
  * { margin: 0; padding: 0; box-sizing: border-box; }
  html, body { width: 1200px; height: 1200px; overflow: hidden; background: var(--navy); }
  .cover {
    position: relative;
    width: 1200px;
    height: 1200px;
    overflow: hidden;
    background-color: var(--navy);
    background-image:
      linear-gradient(to right, var(--grid-line) 1px, transparent 1px),
      linear-gradient(to bottom, var(--grid-line) 1px, transparent 1px);
    background-size: 65px 65px;
    background-position: 1px 1px;
    font-family: "Poppins", sans-serif;
  }
  .decor { position: absolute; inset: 0; width: 1200px; height: 1200px; }

  .show-title {
    position: absolute;
    left: 0; right: 0;
    text-align: center;
    font-family: "Bebas Neue", sans-serif;
    font-weight: 400;
    line-height: 1;
    white-space: nowrap;
  }
  .show-title--top { top: 64px; font-size: 236px; color: var(--white); }
  .show-title--bottom { top: 262px; font-size: 198px; color: var(--gold); letter-spacing: -1px; }

  .photo-frame {
    position: absolute;
    top: 480px;
    width: 360px;
    height: 360px;
    border: 2px solid var(--gold);
  }
  .photo-frame--guest { left: 200px; }
  .photo-frame--host { left: 641px; }
  .photo-slot {
    position: absolute;
    top: 22px; left: 22px;
    width: 312px; height: 312px;
    background: var(--placeholder);
    display: flex;
    align-items: center;
    justify-content: center;
    font-size: 15px;
    font-weight: 500;
    color: var(--placeholder-text);
    letter-spacing: 0.5px;
  }

  .gear-photo {
    position: absolute;
    border-radius: 28px;
    background: linear-gradient(135deg, var(--gear-light), var(--gear-dark));
    opacity: 0.85;
  }
  .gear-photo--headphones-top { left: 1030px; top: 20px; width: 170px; height: 205px; border-radius: 28px 0 0 28px; }
  .gear-photo--headphones-bottom { left: 0; top: 870px; width: 185px; height: 255px; border-radius: 0 28px 28px 0; }
  .gear-photo--microphone { left: 860px; top: 690px; width: 340px; height: 280px; border-radius: 28px 0 0 28px; opacity: 0.9; }

  .guest-credit {
    position: absolute;
    left: 0; right: 0;
    text-align: center;
    color: var(--white);
    white-space: nowrap;
  }
  .guest-credit__with {
    position: absolute;
    left: 440px; top: 938px;
    font-family: "Yellowtail", cursive;
    font-size: 60px;
    line-height: 1;
    color: var(--gold);
    transform: rotate(-8deg);
  }
  .guest-credit__name { top: 984px; font-size: 72px; font-weight: 700; line-height: 1.15; }
  .guest-credit__role { top: 1068px; font-size: 28px; font-weight: 500; line-height: 1.2; }
  .guest-credit__company { top: 1106px; font-size: 33px; font-weight: 400; line-height: 1.2; }
  .show-mark {
    position: absolute;
    left: 556px; top: 893px;
    width: 80px; height: 80px;
    border-radius: 50%;
    border: 6px solid var(--white);
    background: var(--gold);
  }
</style>
</head>
<body>
<main class="cover">
  <svg class="decor" viewBox="0 0 1200 1200" aria-hidden="true">
    <circle cx="240" cy="60" r="640" fill="none" stroke="var(--navy-ring)" stroke-width="70"/>
    <g class="dot-grid" fill="var(--gold)">
      <circle cx="7" cy="408" r="6"/><circle cx="26" cy="408" r="6"/>
      <circle cx="7" cy="430" r="6"/><circle cx="26" cy="430" r="6"/>
      <circle cx="7" cy="452" r="6"/><circle cx="26" cy="452" r="6"/>
      <circle cx="7" cy="474" r="6"/><circle cx="26" cy="474" r="6"/>
      <circle cx="7" cy="496" r="6"/><circle cx="26" cy="496" r="6"/>
    </g>
    <g class="triangle-stack">
      <polygon points="1110,505 1129,529 1091,529" fill="var(--white)"/>
      <polygon points="1110,529 1129,553 1091,553" fill="var(--gold)"/>
      <polygon points="1110,553 1129,577 1091,577" fill="var(--white)"/>
      <polygon points="1110,577 1129,601 1091,601" fill="var(--gold)"/>
      <polygon points="1110,601 1129,625 1091,625" fill="var(--white)"/>
    </g>
    <g class="chevrons" fill="none" stroke="var(--white)" stroke-width="4">
      <polyline points="1054,980 1030,1006 1054,1032"/>
      <polyline points="1080,980 1056,1006 1080,1032"/>
      <polyline points="1106,980 1082,1006 1106,1032"/>
      <polyline points="1132,980 1108,1006 1132,1032"/>
    </g>
    <circle class="corner-disc" cx="1200" cy="1192" r="85" fill="var(--gold)"/>
  </svg>

  <div class="gear-photo gear-photo--headphones-top" role="img" aria-label="Photo of silver studio headphones"></div>
  <div class="gear-photo gear-photo--headphones-bottom" role="img" aria-label="Photo of silver studio headphones"></div>

  <h1 class="show-title show-title--top">HARBOR OF</h1>
  <h1 class="show-title show-title--bottom">KITCHENCRAFT</h1>

  <div class="photo-frame photo-frame--guest">
    <div class="photo-slot" role="img" aria-label="Guest headshot goes here">GUEST’S PHOTO</div>
  </div>
  <div class="photo-frame photo-frame--host">
    <div class="photo-slot" role="img" aria-label="Host headshot goes here">HOST PHOTO</div>
  </div>

  <div class="gear-photo gear-photo--microphone" role="img" aria-label="Photo of a black podcast microphone on a boom arm"></div>

  <div class="show-mark" aria-hidden="true"></div>
  <span class="guest-credit__with">With</span>
  <p class="guest-credit guest-credit__name">MAYA THORNTON</p>
  <p class="guest-credit guest-credit__role">PROFESSIONAL TITLE</p>
  <p class="guest-credit guest-credit__company">HARBOR OF KITCHENCRAFT</p>
</main>
</body>
</html>
```